Marina Web Page

I'm looking for a visually engaging web page/layout that I can use as the basis for a website for my Marina. I need to include page content that can be stored and updated in an include file to allow someone to easily manage content without editing html or needing to understand html.

The business is a small marina and fishing center located on the Pamlico sound in eastern North Carolina right off the Intracoastal Waterway. We offer wet slips with power, water, and wifi and also have powered RV slips for camping available. The Marina sells fuel, beer, tackle/bait, and ice. The Marina also has an island style bar (The Gullwing Bar) and live music most weekends. The bar has a mascot named Tazzo, short for captain, who is a black labradoodle know for diving to the bottom of the marina basin to retrieve oysters and rocks. Tazzo could be incorporated as a minor design element but isn't a requirement.The marina caters to coastal sportsmen interested in sound fishing as well as offshore sport fishing. The Marina also offers fishing charters form a 32' Wavecrest fishing boat w/ tuna tower.

The primary purpose of the initial version of the website is to communicate information about up coming events, music, bar specials etc... It will also be used to feature our services, fishing report and weather info, where we are located from both land and water, and a photo gallery.

Target Market(s)

Coastal sports enthusiast and the coastal boating community

Industry/Entity Type

Business

Requirements
Must have
• I would like animated menus incorporated into the page temple. It must also allow for the updating/storing of page content in a separate file to that an employee of the marina can update specials and events without having to understand or edit html.
Nice to have
• A photo gallery option that will present photos from a folder on the web server. Changing photos should be as easy as adding or deleting photos from the folder.

```html
<!DOCTYPE html>
<html lang="en">
<head>
<meta charset="utf-8">
<title>Harbor Reach Marina</title>
<link href="https://fonts.googleapis.com/css2?family=Montserrat:wght@300;400;500;600&display=swap" rel="stylesheet">
<style>
  :root {
    --ink: #333333;
    --muted: #666666;
    --blue: #3a6db5;
    --cream: #fffcf3;
    --rule: #e2e2e2;
    --dark: #555555;
    --yellow: #f5d63d;
    --footer: #efefef;
    --white: #ffffff;
  }
  * { margin: 0; padding: 0; box-sizing: border-box; }
  html, body { width: 970px; height: 1200px; overflow: hidden; }
  body {
    position: relative;
    font-family: "Montserrat", sans-serif;
    color: var(--ink);
    background: var(--white);
  }
  .abs { position: absolute; }

  .site-header {
    position: absolute; left: 0; top: 0; width: 970px; height: 109px;
    background: linear-gradient(#ffffff, #f3f3f3);
  }
  .brand { left: 105px; top: 46px; display: flex; align-items: center; gap: 8px; }
  .brand-mark { width: 26px; height: 26px; border-radius: 50%; background: #f2c245; }
  .brand-name { font-size: 17px; font-weight: 600; color: var(--blue); letter-spacing: 0.2px; }
  .search {
    left: 666px; top: 34px; width: 199px; height: 20px;
    background: #efefef; border-radius: 2px;
    font-size: 7px; color: #c8c8c8; padding: 6px 8px;
  }
  .search svg { position: absolute; right: 6px; top: 5px; }
  .main-nav { top: 73px; font-size: 12px; color: var(--ink); }
  .main-nav span { position: absolute; white-space: nowrap; }

  .hero {
    left: 0; top: 109px; width: 970px; height: 358px;
    background: linear-gradient(#bfe3f5 0%, #dff0f7 40%, #e8e8e6 52%, #9fb7c9 68%, #2f78b4 85%, #1f5f9e 100%);
  }
  .hero-dots { left: 462px; top: 430px; display: flex; gap: 2px; }
  .hero-dots i { width: 11px; height: 11px; border-radius: 50%; background: #333; border: 1.5px solid #888; display: block; }
  .hero-dots i.on { background: #ddd; border-color: #333; }

  .offers { left: 0; top: 467px; width: 970px; height: 202px; background: var(--cream); }
  .offers-title { left: 0; top: 18px; width: 984px; text-align: center; font-size: 14.5px; font-weight: 500; color: var(--blue); }
  .offers-rule { left: 0; top: 44px; width: 970px; height: 1px; background: #ebe7da; }
  .offer-thumb { top: 55px; width: 178px; height: 103px; }
  .offer-cap { font-size: 11.5px; }

  .section-title { font-size: 14.5px; font-weight: 500; color: var(--blue); }
  .section-rule { height: 1px; background: var(--rule); }
  .body-copy { font-size: 11.3px; line-height: 19.4px; font-weight: 300; color: var(--muted); text-align: justify; }

  .gallery-frame { left: 558px; top: 744px; width: 307px; height: 178px; background: #e4e4e4; border-bottom: 2px solid #cfcfcf; }
  .gallery-photo { left: 6px; top: 6px; width: 295px; height: 166px; background: linear-gradient(#6f8ea3, #8b7a66 60%, #4e4b45); }
  .gallery-arrow { top: 73px; }

  .thumb { top: 985px; width: 83px; height: 58px; }
  .round-btn { top: 1007px; width: 14px; height: 14px; border-radius: 50%; background: #222; }

  .signup { left: 105px; top: 1063px; width: 760px; height: 73px; background: var(--dark); }
  .signup-text { left: 23px; top: 20px; font-size: 18px; font-weight: 300; color: #f2f2f2; white-space: nowrap; }
  .signup-input { left: 313px; top: 22px; width: 322px; height: 33px; background: #fff; font-size: 9px; color: #aaa; padding: 11px 10px; }
  .signup-btn { left: 652px; top: 23px; width: 82px; height: 29px; background: var(--yellow); font-size: 11px; text-align: center; line-height: 29px; color: #333; }

  .site-footer { left: 0; top: 1136px; width: 970px; height: 64px; background: var(--footer); }
  .footer-nav { left: 104px; top: 18px; font-size: 11.5px; white-space: nowrap; }
  .footer-nav b { font-weight: 400; margin: 0 14px; }
  .copyright { left: 105px; top: 38px; font-size: 11.5px; }
  .social { top: 25px; width: 24px; height: 24px; border-radius: 3px; }
</style>
</head>
<body>

<header class="site-header">
  <div class="abs brand"><span class="brand-mark"></span><span class="brand-name">Harbor Reach Marina</span></div>
  <div class="abs search">Search site
    <svg width="9" height="9" viewBox="0 0 9 9"><circle cx="3.6" cy="3.6" r="2.6" fill="none" stroke="#999" stroke-width="1"/><line x1="5.5" y1="5.5" x2="8.5" y2="8.5" stroke="#999" stroke-width="1.3"/></svg>
  </div>
  <nav class="abs main-nav">
    <span style="left:395px">About Us</span>
    <span style="left:483px">Slips</span>
    <span style="left:544px">Amenities</span>
    <span style="left:636px">Affliates</span>
    <span style="left:718px">Boater Info</span>
    <span style="left:816px">Contact</span>
  </nav>
</header>

<div class="abs hero" role="img" aria-label="Marina full of yachts and sailboats reflected in calm blue water"></div>
<div class="abs hero-dots"><i class="on"></i><i></i><i></i><i></i></div>

<section class="abs offers">
  <h2 class="abs offers-title section-title">Camping Offer Available</h2>
  <div class="abs offers-rule"></div>
  <div class="abs offer-thumb" style="left:105px;background:linear-gradient(#7fb2e4,#dfe9f2 55%,#5d5a4e);" role="img" aria-label="Sailboats docked in wet slips"></div>
  <div class="abs offer-thumb" style="left:299px;background:linear-gradient(#a9c9e6,#2f6d97 55%,#d9dfe3);" role="img" aria-label="Aerial view of marina water and boats"></div>
  <div class="abs offer-thumb" style="left:493px;background:linear-gradient(135deg,#e9e2dc,#3f6fc9 55%,#d85c4f);" role="img" aria-label="Laptop on a boat deck for wifi"></div>
  <div class="abs offer-thumb" style="left:687px;background:linear-gradient(#8bb8e0,#bcd0de 50%,#1f4e7a);" role="img" aria-label="Boats moored beside RV slips"></div>
  <p class="abs offer-cap" style="left:105px;top:177px">Wet slips with power</p>
  <p class="abs offer-cap" style="left:299px;top:177px">Water</p>
  <p class="abs offer-cap" style="left:494px;top:177px">Wifi</p>
  <p class="abs offer-cap" style="left:686px;top:171px">Powered RV slips</p>
</section>

<h2 class="abs section-title" style="left:105px;top:702px">Welcome to Harbor Reach Marina</h2>
<div class="abs section-rule" style="left:105px;top:733px;width:437px"></div>
<div class="abs" style="left:105px;top:744px;width:437px;height:178px;background:linear-gradient(#4f6a7d,#3a5468 60%,#cfd9e0);" role="img" aria-label="Sport fishing boat with tuna tower speeding across the water"></div>
<p class="abs body-copy" style="left:106px;top:938px;width:436px">Tie up at our wet slips just off the Intracoastal Waterway and stay for the fun. Live music plays at The Gullwing Bar most weekends, with bar specials posted every Friday. Check our events calendar for tournaments and cookouts, read the latest sound and offshore fishing report, and see today's weather before you head out. Fuel, beer, bait, tackle and ice are sold at the dock.</p>

<h2 class="abs section-title" style="left:558px;top:702px">Photo Gallery</h2>
<div class="abs section-rule" style="left:558px;top:733px;width:307px"></div>
<div class="abs gallery-frame">
  <div class="abs gallery-photo" role="img" aria-label="Waterfront building with decks and a boat at the dock"></div>
  <svg class="abs gallery-arrow" style="left:17px" width="18" height="26" viewBox="0 0 18 26"><polyline points="15,2 4,13 15,24" fill="none" stroke="#f5c93a" stroke-width="5"/></svg>
  <svg class="abs gallery-arrow" style="left:272px" width="18" height="26" viewBox="0 0 18 26"><polyline points="3,2 14,13 3,24" fill="none" stroke="#f5c93a" stroke-width="5"/></svg>
</div>
<p class="abs body-copy" style="left:559px;top:938px;width:306px">See the latest catches, dockside events and weekend music nights.</p>

<svg class="abs round-btn" style="left:561px" viewBox="0 0 14 14"><circle cx="7" cy="7" r="7" fill="#222"/><polyline points="8.5,4 5.5,7 8.5,10" fill="none" stroke="#fff" stroke-width="1.6"/></svg>
<div class="abs thumb" style="left:578px;background:linear-gradient(#cfe0c0,#3c3b38);" role="img" aria-label="Black labradoodle mascot on the grass"></div>
<div class="abs thumb" style="left:669px;background:linear-gradient(#c9d3db,#5d6a70);" role="img" aria-label="Dock and calm water"></div>
<div class="abs thumb" style="left:761px;background:linear-gradient(#e8a06f,#9e4a4a 60%,#5a2e3a);" role="img" aria-label="Marina at sunset"></div>
<svg class="abs round-btn" style="left:848px" viewBox="0 0 14 14"><circle cx="7" cy="7" r="7" fill="#222"/><polyline points="5.5,4 8.5,7 5.5,10" fill="none" stroke="#fff" stroke-width="1.6"/></svg>

<section class="abs signup">
  <p class="abs signup-text">Get our weekly fishing report</p>
  <div class="abs signup-input">Enter Your E-mail address</div>
  <div class="abs signup-btn">SUBMIT</div>
</section>

<footer class="abs site-footer">
  <p class="abs footer-nav">About Us<b>|</b>Slips<b>|</b>Amenities<b>|</b>Affliates<b>|</b>Boater Info<b>|</b>Contact</p>
  <p class="abs copyright">©2013 Company Name , All Rights Reserved</p>
  <div class="abs social" style="left:738px;background:#f08a24" aria-label="Feed"></div>
  <div class="abs social" style="left:772px;background:#5cc3ea" aria-label="Social link"></div>
  <div class="abs social" style="left:806px;background:#3b5b9a" aria-label="Social link"></div>
  <div class="abs social" style="left:841px;background:#f26a21" aria-label="Blog"></div>
</footer>

</body>
</html>
```